Velmora Link needs a brochure review

We are a company operating in more than 10 countries that, since 1972, has the ambitious and innovative objective to stimulate foreign language learning by discovering different countries and cultures, through training courses tailored to individual needs
We need a layout review of our brochure in order to make the content clearer, immediate and appealing and, at the same time, make the layout more modern and young.
The pages we need are: the cover and pages 3, 5, 7, 20, 21, 22, 23, 34, 36, 37. You will find our actual brochure pdf as attachment

Target Market(s)

Students and families, business

Industry/Entity Type

It Company

Requirements
Must have
• The same written information as the actual one.
• Blue and green colours.
• The cover must be simple, elegant and clean but new and effective. In addition to the cover the pages you should review are number :2, 3, 4, 5, 6, 7. Feel free to use new background, images and new layout for the text.

```html
<!DOCTYPE html>
<html lang="it">
<head>
<meta charset="utf-8">
<title>Velmora Link – Estate 2017</title>
<link rel="stylesheet" href="https://fonts.googleapis.com/css2?family=Alegreya+Sans+SC:wght@400;500&display=swap">
<style>
  :root {
    --blue: #1a68ad;
    --green: #8cc63f;
    --ink: #1d1d1d;
    --label-dark: #d6d6d6;
    --label-light: #ebebeb;
    --abroad-dark: #7a9cb9;
    --abroad-light: #88b2cf;
    --italy-dark: #c6ee84;
    --italy-light: #e0f8b9;
  }
  html, body { margin: 0; padding: 0; overflow: hidden; }
  .page {
    position: relative;
    width: 976px; height: 1200px;
    overflow: hidden;
    font-family: "Alegreya Sans SC", sans-serif;
    color: var(--ink);
    background: #f4f5f3;
  }
  .backdrop {
    position: absolute; inset: 0;
    background:
      linear-gradient(180deg, rgba(255,255,255,0.92) 0%, rgba(255,255,255,0.55) 25%, rgba(236,232,222,0.6) 60%, rgba(226,230,218,0.7) 100%),
      linear-gradient(90deg, #e6e2d6 0%, #efece4 45%, #e3dfd3 100%);
  }
  .title {
    position: absolute; left: 40px; top: 34px; margin: 0;
    font-weight: 400; font-size: 51px; line-height: 48px;
    color: var(--blue); letter-spacing: 0.5px;
  }
  .copy {
    position: absolute; left: 40px; margin: 0;
    font-size: 19px; line-height: 21.7px; letter-spacing: 0.4px;
  }
  .intro { top: 281px; width: 880px; }
  .note-school { top: 823px; width: 880px; }
  .note-tour { top: 910px; width: 880px; }
  .compare {
    position: absolute; left: 40px; top: 426px;
    border-collapse: separate; border-spacing: 0;
    font-size: 30px;
  }
  .compare th, .compare td { padding: 0; height: 37.6px; line-height: 37.6px; }
  .compare thead th { height: 37px; font-weight: 400; padding-bottom: 16px; }
  .compare thead .col-gap { background: none; }
  .compare .head-abroad { background: var(--abroad-dark); color: var(--green); background-clip: content-box; }
  .compare .head-italy { background: var(--italy-light); color: var(--blue); background-clip: content-box; }
  .compare .label { width: 462px; padding-left: 3px; text-align: left; font-weight: 400; }
  .compare .spacer { width: 8px; }
  .compare .abroad { width: 192px; text-align: center; }
  .compare .italy { width: 226px; text-align: center; }
  .compare tbody tr:nth-child(odd) .label { background: var(--label-dark); }
  .compare tbody tr:nth-child(even) .label { background: var(--label-light); }
  .compare tbody tr:nth-child(odd) .abroad { background: var(--abroad-dark); }
  .compare tbody tr:nth-child(even) .abroad { background: var(--abroad-light); }
  .compare tbody tr:nth-child(odd) .italy { background: var(--italy-dark); }
  .compare tbody tr:nth-child(even) .italy { background: var(--italy-light); }
  .compare .total-abroad { color: var(--green); }
  .compare .total-italy { color: var(--blue); }
  .folio {
    position: absolute; right: 56px; top: 1148px;
    font-size: 21px; letter-spacing: 0.4px;
  }
</style>
</head>
<body>
<div class="page">
  <div class="backdrop" role="img" aria-label="Foto sbiadita delle rovine del Foro Romano con colonne antiche e visitatori"></div>

  <h1 class="title">PerchÉ 2 settimane all'estero<br>equivalgono ad un anno scolastico<br>in Italia</h1>

  <p class="copy intro">I numeri non mentono! Durante una vacanza studio di 14 giorni&nbsp; all'estero, sarai esposto alla lingua straniera tanto quanto durante un intero anno a scuala in Italia, e ovviamente in modo molto più mirato ed efficiente.</p>

  <table class="compare">
    <thead>
      <tr>
        <th class="label col-gap"></th>
        <th class="spacer col-gap"></th>
        <th class="abroad head-abroad">all'estero</th>
        <th class="spacer col-gap"></th>
        <th class="italy head-italy">In Italia</th>
      </tr>
    </thead>
    <tbody>
      <tr><th class="label">Giorni</th><td class="spacer"></td><td class="abroad">14</td><td class="spacer"></td><td class="italy">200</td></tr>
      <tr><th class="label">Studenti in classe</th><td class="spacer"></td><td class="abroad">12</td><td class="spacer"></td><td class="italy">25</td></tr>
      <tr><th class="label">Ore di lezione</th><td class="spacer"></td><td class="abroad">40</td><td class="spacer"></td><td class="italy">90</td></tr>
      <tr><th class="label">Ore di verifiche in classe</th><td class="spacer"></td><td class="abroad">-</td><td class="spacer"></td><td class="italy">45</td></tr>
      <tr><th class="label">Ore di attività in inglese</th><td class="spacer"></td><td class="abroad">100</td><td class="spacer"></td><td class="italy">-</td></tr>
      <tr><th class="label">Insegnanti</th><td class="spacer"></td><td class="abroad">Inglesi</td><td class="spacer"></td><td class="italy">Italiani</td></tr>
      <tr><th class="label">Totale ore di apprendimento</th><td class="spacer"></td><td class="abroad total-abroad">140</td><td class="spacer"></td><td class="italy total-italy">45</td></tr>
    </tbody>
  </table>

  <p class="copy note-school">I programmi di lingua inglese della scuola italiana prevendono circa 90 lezioni all'anno con classi composti da 25 studenti. Considerando le ore dedicate a verifche e interrogazioni, il numero di lezioni effettive si reduce di circa il 50%</p>

  <p class="copy note-tour">Una vacanza studio Velmora Link di 2 settimane prevede 20 lezioni a settimana con docenti madrelingua, senza verifiche o interrogazioni e in classi di non più di 15 studenti, di diverse nazionalità. Considerando che tutte le attività, anche quelle extrascolastiche, sonos volte in inglese, l'apprendimento della lingua risulta maggioree più efficace.</p>

  <div class="folio">Velmora Link Estate 2017 - 2</div>
</div>
</body>
</html>
```